Morvela Aesthetic Doctor

I require an elegant, luxurious looking business card for my aesthetic business. I am a doctor and that will set me aside from competitors. I am planning to provide home and spa based treatments to clients with high expectations. I have attached my logo.

```html
<!DOCTYPE html>
<html lang="en">
<head>
<meta charset="utf-8">
<title>Morvela Aesthetic Doctor – Business Card</title>
<link href="https://fonts.googleapis.com/css2?family=Open+Sans:wght@300;400&display=swap" rel="stylesheet">
<style>
  :root {
    --backdrop: #dadada;
    --card: #fefdf7;
    --ink-grey: #9a9ea3;
    --rule-grey: #b9bcbf;
    --accent-blue: #1aa3e8;
  }
  * { box-sizing: border-box; margin: 0; padding: 0; }
  html, body {
    width: 1200px; height: 873px; overflow: hidden;
    background: var(--backdrop);
    font-family: "Open Sans", Arial, sans-serif;
  }
  .sheet {
    position: relative; width: 1200px; height: 873px;
    display: flex; align-items: center; justify-content: center; gap: 60px;
  }
  .card {
    position: relative; width: 500px; height: 286px;
    background: var(--card);
    box-shadow: 0 8px 24px rgba(0,0,0,0.12);
  }

  /* Details side */
  .card-details { padding: 26px 30px 0 30px; }
  .identity { text-align: right; }
  .identity .doctor-name {
    font-weight: 300; font-size: 27px; color: var(--ink-grey); line-height: 1.1;
  }
  .identity .credential {
    font-weight: 400; font-size: 12.5px; color: var(--accent-blue); line-height: 1.45;
  }
  .identity .credential:first-of-type { margin-top: 6px; }
  .contact-list { list-style: none; margin-top: 12px; text-align: right; }
  .contact-list li {
    display: flex; justify-content: flex-end; align-items: center; gap: 8px;
    font-weight: 300; font-size: 14px; color: var(--ink-grey); line-height: 1.25;
  }
  .contact-list svg { width: 12px; height: 12px; flex: none; }
  .divider { height: 1px; background: var(--rule-grey); margin: 12px 0 10px; }
  .services {
    display: grid; grid-template-columns: 180px 1fr; column-gap: 20px;
  }
  .services ul { list-style: none; }
  .services li {
    display: flex; align-items: center; gap: 7px;
    font-weight: 300; font-size: 13px; color: var(--ink-grey); line-height: 1.45;
  }
  .services svg { width: 12px; height: 10px; flex: none; }

  /* Brand side */
  .card-brand { display: flex; align-items: center; justify-content: center; gap: 16px; }
  .brand-dot { width: 46px; height: 46px; border-radius: 50%; background: var(--accent-blue); }
  .brand-name {
    font-weight: 300; font-size: 30px; color: var(--ink-grey);
    letter-spacing: 1px; line-height: 1.15;
  }
  .brand-name span { display: block; font-size: 15px; letter-spacing: 3px; }
</style>
</head>
<body>
<main class="sheet">
  <section class="card card-details" aria-label="Card back with contact details">
    <div class="identity">
      <p class="doctor-name">Dr Elise Varnholt</p>
      <p class="credential">MRCPCH MD</p>
      <p class="credential">Australasian Diploma of Aesthetic Medicine</p>
    </div>
    <ul class="contact-list">
      <li>0800 437 915
        <svg viewBox="0 0 12 12" fill="none" stroke="var(--accent-blue)" stroke-width="1.2"><path d="M3 1.5 L4.8 3.6 L3.8 4.8 Q5 7.2 7.2 8.2 L8.4 7.2 L10.5 9 L9.3 10.5 Q4.5 10 1.5 3 Z"/></svg>
      </li>
      <li>elise@morvela.co.nz
        <svg viewBox="0 0 12 12" fill="none" stroke="var(--accent-blue)" stroke-width="1.2"><rect x="1" y="2.5" width="10" height="7"/><path d="M1 2.5 L6 6.5 L11 2.5"/></svg>
      </li>
      <li>www.morvela.co.nz
        <svg viewBox="0 0 12 12" fill="none" stroke="var(--accent-blue)" stroke-width="1.1"><circle cx="6" cy="6" r="5"/><ellipse cx="6" cy="6" rx="2.2" ry="5"/><path d="M1 6 H11 M2 3.5 H10 M2 8.5 H10"/></svg>
      </li>
    </ul>
    <div class="divider"></div>
    <div class="services">
      <ul>
        <li><svg viewBox="0 0 12 10" fill="none" stroke="var(--accent-blue)" stroke-width="1"><path d="M3 1 H9 L11 3.5 L6 9 L1 3.5 Z M1 3.5 H11 M4.5 1 L6 9 L7.5 1"/></svg>Dermal injectables</li>
        <li><svg viewBox="0 0 12 10" fill="none" stroke="var(--accent-blue)" stroke-width="1"><path d="M3 1 H9 L11 3.5 L6 9 L1 3.5 Z M1 3.5 H11 M4.5 1 L6 9 L7.5 1"/></svg>Plasma facials</li>
        <li><svg viewBox="0 0 12 10" fill="none" stroke="var(--accent-blue)" stroke-width="1"><path d="M3 1 H9 L11 3.5 L6 9 L1 3.5 Z M1 3.5 H11 M4.5 1 L6 9 L7.5 1"/></svg>Microneedling</li>
      </ul>
      <ul>
        <li><svg viewBox="0 0 12 10" fill="none" stroke="var(--accent-blue)" stroke-width="1"><path d="M3 1 H9 L11 3.5 L6 9 L1 3.5 Z M1 3.5 H11 M4.5 1 L6 9 L7.5 1"/></svg>Skin boosters</li>
        <li><svg viewBox="0 0 12 10" fill="none" stroke="var(--accent-blue)" stroke-width="1"><path d="M3 1 H9 L11 3.5 L6 9 L1 3.5 Z M1 3.5 H11 M4.5 1 L6 9 L7.5 1"/></svg>Excessive sweating</li>
        <li><svg viewBox="0 0 12 10" fill="none" stroke="var(--accent-blue)" stroke-width="1"><path d="M3 1 H9 L11 3.5 L6 9 L1 3.5 Z M1 3.5 H11 M4.5 1 L6 9 L7.5 1"/></svg>Home and Spa Based Treatments</li>
      </ul>
    </div>
  </section>

  <section class="card card-brand" aria-label="Card front with brand name">
    <div class="brand-dot"></div>
    <p class="brand-name">MORVELA<span>AESTHETIC DOCTOR</span></p>
  </section>
</main>
</body>
</html>
```